Business Consulting Company requires a website design (PSD+HTML+CSS required)

Tarnvale Advisory is a Business Consulting Company that provides Analysis, Business Coaching and Systems and Document Design for clients.

We would like a simplistic yet professional looking website design that uses high quality imagery to project a professional persona across our entire site.

The completed project will need to include PSD files (for editing in Photoshop) and will need to also include HTML+CSS coded files that can be edited in Adobe Dreamweaver CS5.5.

Tarnvale Advisory currently has a functioning website (located at www.tarnvaleadvisory.com.au) but would like to replace its current site with something more professional, user friendly and content simplistic, with the overall design of this project being clean and very easy to navigate whilst remaining professionally focused.

A brief has been attached to this project to provide the key details but please feel free to contact me if you require any clarification or have any questions regarding the project.

Target Market(s)

The target audience for this website will be small to medium sized businesses (of all descriptions).

Industry/Entity Type

Business

Coding

Coded - Design and coding required

Number of Pages Required

5+ page

Requirements
Must have
• Simplistic design structure
• Professional images
• Easy to navigate
• Must be uploaded in PSD format
• Must be coded (HTML+CSS) and compatible with Adobe Dreamweaver CS5.5
Nice to have
• Use of the Company’s corporate colours throughout the site design
• Adding a Home page slider bar with images and short catchy messages (i.e. text based statements)
• Having a quick link box on each page that provides easy navigation throughout the site
• The use of different icons and images to depict our different services (i.e. a different icon and image for analysis service and coaching service etc.).
• All pages should follow a similar theme (universal approach to all pages)
Should not have
• When coding, images should not be used in place of text (all text must be editable)

```html
<!DOCTYPE html>
<html lang="en">
<head>
<meta charset="utf-8">
<title>Tarnvale Advisory</title>
<link href="https://fonts.googleapis.com/css2?family=Arimo:wght@400;700&family=Michroma&family=Open+Sans:wght@400;600&family=Roboto+Condensed:wght@400;700&display=swap" rel="stylesheet">
<style>
:root{
  --blue:#3d96d8;
  --blue-band:#4499d9;
  --blue-dark:#2f86c8;
  --blue-box:#5aa7e0;
  --text:#333;
  --muted:#888;
  --line:#dcdcdc;
  --footer:#161616;
  --white:#fff;
}
*{margin:0;padding:0;box-sizing:border-box}
html,body{width:861px;height:1200px;overflow:hidden}
body{position:relative;background:var(--white);font-family:Arimo,Arial,sans-serif;color:var(--text)}
.abs{position:absolute}
.topline{left:0;top:0;width:861px;height:3px;background:var(--blue)}
.brand{left:94px;top:30px;display:flex;align-items:center;gap:10px}
.brand-dot{width:34px;height:34px;border-radius:50%;background:var(--blue)}
.brand-name{font-family:"Open Sans",sans-serif;font-size:21px;font-weight:400;color:#555;letter-spacing:.5px}
.phone{right:95px;top:14px;display:flex;align-items:center;gap:8px;font-family:"Open Sans",sans-serif;font-size:11px;color:#444}
.nav{right:94px;top:53px;display:flex;gap:26px;font-family:"Open Sans",sans-serif;font-size:9.5px;color:#333;list-style:none}
.nav .active{color:var(--blue)}
.hero{left:0;top:94px;width:861px;height:374px;background:#000;overflow:hidden}
.hero-art{position:absolute;left:400px;top:0;width:461px;height:374px;background:radial-gradient(ellipse at 60% 42%,#9fe4ff 0%,#2aa5e0 22%,#0d5a8a 48%,#03121c 78%,#000 100%)}
.hero-title{position:absolute;left:78px;top:120px;font-family:Michroma,sans-serif;color:var(--white);font-size:27px;line-height:44px;letter-spacing:1px}
.btn{position:absolute;left:77px;top:226px;width:103px;height:32px;background:var(--blue);border-radius:3px;color:var(--white);font-family:"Roboto Condensed",sans-serif;font-size:13px;line-height:32px;text-align:center;box-shadow:0 2px 0 #1f6ea8}
.arrow{position:absolute;top:170px}
.section-title{left:94px;top:490px;display:flex;align-items:center;gap:12px;font-family:"Roboto Condensed",sans-serif;font-weight:700;font-size:18px;color:#444}
.section-title span{color:var(--blue)}
.card{position:absolute;top:558px;width:161px;height:272px;border:1px solid var(--line);background:var(--white)}
.card-icon{position:absolute;left:53px;top:-29px;width:54px;height:54px;border-radius:50%;background:var(--white);border:1px solid var(--line);display:flex;align-items:center;justify-content:center}
.card-photo{position:absolute;left:11px;top:35px;width:139px;height:98px;border:2px solid #eee;box-shadow:0 1px 3px rgba(0,0,0,.15)}
.card h3{position:absolute;left:10px;right:8px;top:148px;font-family:"Roboto Condensed",sans-serif;font-weight:400;font-size:13px;line-height:16px;color:var(--blue)}
.card p{position:absolute;left:10px;right:10px;font-size:7.6px;line-height:16.8px;color:var(--muted);text-align:justify}
.band{left:0;top:858px;width:861px;height:286px;background:var(--blue-band);color:var(--white)}
.band h2{position:absolute;font-family:"Open Sans",sans-serif;font-weight:400;font-size:17px;display:flex;align-items:center;gap:10px}
.welcome p{position:absolute;left:94px;width:412px;font-size:7.6px;line-height:16px}
.quote{position:absolute;left:533px;top:60px;width:234px;height:88px;background:var(--blue-box);padding:12px 14px 0 30px;font-size:7.6px;line-height:16px}
.quote::after{content:"";position:absolute;left:40px;bottom:-7px;border:7px solid transparent;border-bottom:0;border-top-color:var(--blue-box)}
.quote-mark{position:absolute;left:12px;top:8px;font-size:18px;font-family:Georgia,serif}
.author{position:absolute;left:571px;top:162px;font-size:8px;font-style:italic}
.divider{position:absolute;left:18px;top:204px;width:843px;height:1px;background:rgba(255,255,255,.25)}
.contacts{position:absolute;left:94px;top:236px;width:674px;display:flex;justify-content:space-between;font-size:8.4px}
.contacts li{list-style:none;display:flex;align-items:center;gap:9px}
.contacts a{color:var(--white)}
.footer{left:0;top:1144px;width:861px;height:56px;background:var(--footer);color:#aaa;font-size:8.4px}
.footer .copy{position:absolute;left:96px;top:22px}
.social{position:absolute;right:94px;top:14px;display:flex;gap:11px}
.social span{width:24px;height:24px;border:1px solid #777;border-radius:50%}
</style>
</head>
<body>
<div class="abs topline"></div>

<header>
  <div class="abs brand"><span class="brand-dot"></span><span class="brand-name">Tarnvale Advisory</span></div>
  <div class="abs phone">
    <svg width="18" height="18" viewBox="0 0 18 18"><circle cx="9" cy="9" r="8" fill="none" stroke="#3d96d8" stroke-width="1.2"/><path d="M6 5c-.8.8-.6 2.5 1 4.4s3.6 2.6 4.6 1.6l-1.3-1.3-1 .5C8.5 9.7 7.9 9 7.6 8.2l.6-1z" fill="#3d96d8"/></svg>
    0352 418 907
  </div>
  <ul class="abs nav">
    <li class="active">HOME</li><li>ABOUT US</li><li>SERVICES</li><li>CONTACT US</li><li>TESTIMONIALS</li>
  </ul>
</header>

<section class="abs hero">
  <div class="hero-art" role="img" aria-label="Glowing blue clock face floating above an open hand on a dark background"></div>
  <h1 class="hero-title">GET TIME BACK<br>IN YOUR BUSINESS</h1>
  <div class="btn">READ MORE</div>
  <svg class="arrow" style="left:24px" width="16" height="30" viewBox="0 0 16 30"><path d="M14 2 2 15l12 13" fill="none" stroke="#fff" stroke-width="1.5"/></svg>
  <svg class="arrow" style="left:820px" width="16" height="30" viewBox="0 0 16 30"><path d="M2 2l12 13L2 28" fill="none" stroke="#fff" stroke-width="1.5"/></svg>
</section>

<h2 class="abs section-title">
  <svg width="24" height="24" viewBox="0 0 24 24"><circle cx="9" cy="15" r="6" fill="none" stroke="#ccc" stroke-width="3" stroke-dasharray="3 2"/><circle cx="18" cy="6" r="4" fill="none" stroke="#ccc" stroke-width="2.5" stroke-dasharray="2 1.5"/></svg>
  OUR <span>SERVICES</span>
</h2>

<article class="card" style="left:94px">
  <div class="card-icon"><svg width="34" height="34" viewBox="0 0 34 34"><circle cx="17" cy="17" r="15" fill="none" stroke="#3d96d8" stroke-width="2.5" stroke-dasharray="70 10"/><path d="M11 22v-6M15 22v-9M19 22v-5M23 22v-8" stroke="#3d96d8" stroke-width="2.5"/></svg></div>
  <div class="card-photo" role="img" aria-label="Business team meeting around a table" style="background:linear-gradient(135deg,#d8d2c8,#7a6a5e 55%,#2b2b32)"></div>
  <h3>BUSINESS ANALYSIS</h3>
  <p style="top:172px">Pinpoint critical goals and objectives to bring about maximum profitability and productivity through Tarnvale's in depth and comprehensive business analysis reports.</p>
</article>

<article class="card" style="left:265px">
  <div class="card-icon"><svg width="34" height="34" viewBox="0 0 34 34"><circle cx="17" cy="17" r="15" fill="none" stroke="#3d96d8" stroke-width="2.5" stroke-dasharray="70 10"/><path d="M8 17l5-4 4 2 4-2 5 4-6 5-3-2-3 2z" fill="#3d96d8"/></svg></div>
  <div class="card-photo" role="img" aria-label="Coach presenting at a flip chart to a seated group" style="background:linear-gradient(135deg,#f2f4f6,#c9d3dc 55%,#6f8aa3)"></div>
  <h3>BUSINESS COACHING</h3>
  <p style="top:172px">Transfer essential business knowledge into your business, Brainstorm new and existing concepts, or develop and implement specific strategies via Tarnvale's one...</p>
</article>

<article class="card" style="left:436px">
  <div class="card-icon"><svg width="34" height="34" viewBox="0 0 34 34"><circle cx="17" cy="17" r="15" fill="none" stroke="#3d96d8" stroke-width="2.5" stroke-dasharray="70 10"/><rect x="12" y="9" width="10" height="14" rx="1" fill="none" stroke="#3d96d8" stroke-width="1.8"/><path d="M14 14h6M14 17h6M14 20h4" stroke="#3d96d8" stroke-width="1.3"/></svg></div>
  <div class="card-photo" role="img" aria-label="Smiling businesswoman at her desk" style="background:linear-gradient(135deg,#6c5a4c,#c9b9a7 50%,#8a8580)"></div>
  <h3>BUSINESS SYSTEM DESIGN AND DOCUMENT</h3>
  <p style="top:188px">Save time, money and free up valuable resources by outsourcing your business system or document creation projects to us.</p>
</article>

<article class="card" style="left:606px">
  <div class="card-icon"><svg width="34" height="34" viewBox="0 0 34 34"><circle cx="17" cy="17" r="15" fill="none" stroke="#3d96d8" stroke-width="2.5" stroke-dasharray="70 10"/><path d="M23 10c-5 0-9 4-10 9l2 2c5-1 9-5 9-10zM13 19l-3 1M15 21l-1 3" fill="none" stroke="#3d96d8" stroke-width="1.6"/></svg></div>
  <div class="card-photo" role="img" aria-label="Group of professionals gathered in a bright office" style="background:linear-gradient(135deg,#e6ecef,#a9b8c2 55%,#505c68)"></div>
  <h3>NEW BUSINESS START-UP PACKAGES</h3>
  <p style="top:188px">Starting a new business? Tarnvale provides simplistic, hassle free and easy to administer start-up packages that are a perfect...</p>
</article>

<section class="abs band">
  <div class="welcome">
    <h2 style="left:94px;top:30px"><svg width="18" height="16" viewBox="0 0 18 16"><path d="M9 1 1 8h2v7h4v-4h4v4h4V8h2z" fill="#6fb1e4"/></svg>WELCOME TO TARNVALE ADVISORY</h2>
    <p style="top:68px">Tarnvale Advisory is a business analysis, coaching and business development provider who specialises in assisting businesses to achieve maximum efficiency, increased productivity and who can assist with improving a business's overall profitability.</p>
    <p style="top:126px">At Tarnvale, we pride ourselves on our ability to form strong client relationships whilst delivering impressive results. For us, it's all about effective communication coupled with practical and measurable results!</p>
  </div>
  <h2 style="left:533px;top:30px"><svg width="18" height="16" viewBox="0 0 18 16"><rect x="1" y="4" width="11" height="8" fill="#6fb1e4"/><rect x="6" y="1" width="11" height="8" fill="#6fb1e4" opacity=".7"/></svg>OUR TESTIMONIALS</h2>
  <svg class="abs" style="left:746px;top:34px" width="22" height="12" viewBox="0 0 22 12"><path d="M6 1 1 6l5 5" fill="none" stroke="#fff" stroke-width="2"/><path d="M16 1l5 5-5 5" fill="none" stroke="#6fb1e4" stroke-width="2"/></svg>
  <div class="quote"><span class="quote-mark">&ldquo;</span>We envisage a simplistic design on this page with possibly a single image accompanied by some text that we can separate to depict the testimonials from each client We envisage</div>
  <div class="author">Dana Whitcombe</div>
  <div class="divider"></div>
  <ul class="contacts">
    <li><svg width="12" height="10" viewBox="0 0 12 10"><path d="M1 3c3-3 7-3 10 0v2H8V4H4v1H1z M3 5h6l1 4H2z" fill="#fff"/></svg>03 5241 8907 (Phone)</li>
    <li><svg width="12" height="11" viewBox="0 0 12 11"><rect x="3" y="0" width="6" height="3" fill="#fff"/><rect x="1" y="3" width="10" height="5" fill="#fff"/><rect x="3" y="7" width="6" height="4" fill="none" stroke="#fff"/></svg>03 5241 8908 (Fax)</li>
    <li><svg width="12" height="9" viewBox="0 0 12 9"><rect x=".5" y=".5" width="11" height="8" fill="none" stroke="#fff"/><path d="M.5.5 6 5l5.5-4.5" fill="none" stroke="#fff"/></svg><a>admin@tarnvaleadvisory.com.au</a></li>
    <li><svg width="9" height="12" viewBox="0 0 9 12"><path d="M4.5 12S0 6.5 0 4.5a4.5 4.5 0 0 1 9 0C9 6.5 4.5 12 4.5 12z" fill="#fff"/><circle cx="4.5" cy="4.5" r="1.6" fill="#4499d9"/></svg>PO Box 4270, Moewell, Victoria, Australia 3861</li>
  </ul>
</section>

<footer class="abs footer">
  <div class="copy">&copy; Copy Rights 2014 - Tarnvale Advisory . All rights reserved</div>
  <div class="social"><span></span><span></span><span></span></div>
</footer>
</body>
</html>
```